Poster for company's 5 NORMS

Good Day,

My name is Rilo and I am working for Morvane & Tolbrick Offshore Pte Ltd. We are in the Marine and Offshore industry and based in Singapore.

I have to submit a few A-2 sized poster design samples reflecting our 5 norms to my boss in 40 hours time. So I need your help.

The 5 norms are: (1) Ownership, (2) Positive Mindset, (3) Actions, (4) Teamwork, (5) Honesty.

My company logo can be googled. The corporate colours of the company are blue and grey predominantly and white is occasionally used. But feel free to play with colours. No need to stick to grey, blue and white. The words and headers, you can play with colours too. This poster must be an attention grabber. You can make it look professional yet fun as well.

A few of the poster designs should be build based on the following:
a) 2 liner headers reading the following:
Line 1: Our Winning 5 Norms!
LIne 2: OWNing the P.A.T.H to Tier 1

b) Bottom centre - company's logo

c) Design 1: A winding road (limit to 2 turns) as background and the 5 norms spread vertically along the winding road.

d) Design 2: A circle divided into 5 equal segments and in each segment, the 5 norms.

You should consider highlighting for the initial letter (s) of each word (OWN, P, A, T, H) so that it will reemphasize Owning the Path. Also, attached is a design for the poster that we have on our walls now. I did not scan it properly but I would want a much much better poster.

Please feel free to be creative, especially for the other designs.

Thank you very much. Looking forward to see posters in my inbox.

Have a great day ahead,

Regards, Rilo

Hp: 65-93172548

Good Day,

I just attached a picture of our current poster. I did not scan it well, apologies for that. But we would want a much much better poster.

Thank you!

Hello guys,

I have attached a picture of the company's logo. You can also visit the link below to get the correct logo.

It should state "Morvane & Tolbrick Offshore".

Thanks.

https://www.quorvelsearch.example/search?q=morvane+and+tolbrick+offshore+logo&hl=en-SG&source=lnms&tbm=isch&sa=X&ei=Kp7WQrLMPdazqfht4hJ9Rf&ved=0DBlR_BVpBQ&biw=1366&bih=636&dpr=1

Target Market(s)

Internal stakeholders. Good if it can impress clients as well.

Industry/Entity Type

Industry

Font styles to use
Serif

```html
<!DOCTYPE html>
<html lang="en">
<head>
<meta charset="utf-8">
<title>Our 5 Winning Norms</title>
<link href="https://fonts.googleapis.com/css2?family=Roboto+Condensed:wght@700&family=Roboto+Slab:wght@300;400;700&display=swap" rel="stylesheet">
<style>
  :root {
    --norm-blue: #1a5f9e;
    --band-grey: #b1b1b1;
    --icon-grey: #9a9a9a;
    --paper: #ffffff;
    --ink-dark: #2b3247;
  }
  html, body {
    margin: 0;
    padding: 0;
    overflow: hidden;
  }
  body {
    width: 927px;
    height: 1200px;
    background: var(--paper);
    position: relative;
  }
  .poster {
    position: relative;
    width: 927px;
    height: 1200px;
    overflow: hidden;
  }
  .rule {
    position: absolute;
    left: 0;
    width: 927px;
    background: var(--band-grey);
  }
  .rule--top { top: 46px; height: 13px; }
  .rule--bottom { top: 261px; height: 14px; }
  .header-band {
    position: absolute;
    left: 0;
    top: 65px;
    width: 927px;
    height: 188px;
    background: var(--band-grey);
    text-align: center;
  }
  .headline {
    margin: 0;
    padding-top: 48px;
    font-family: "Roboto Condensed", "Arial Narrow", sans-serif;
    font-weight: 700;
    font-size: 64px;
    line-height: 1;
    letter-spacing: 0.5px;
    color: var(--norm-blue);
  }
  .subline {
    margin: 14px 0 0;
    font-family: "Roboto Slab", Georgia, serif;
    font-weight: 300;
    font-size: 26px;
    letter-spacing: 7px;
    color: #2e2e2e;
  }
  .norm-wheel {
    position: absolute;
    left: 0;
    top: 0;
    width: 927px;
    height: 1200px;
  }
  .norm-label {
    font-family: "Roboto Slab", Georgia, serif;
    font-weight: 300;
    font-size: 28px;
    letter-spacing: 4px;
    fill: var(--norm-blue);
  }
  .norm-initial { font-weight: 700; }
  .segment { fill: var(--norm-blue); }
  .divider { stroke: var(--paper); stroke-width: 7; }
  .icon { fill: var(--icon-grey); }
  .icon-line { fill: none; stroke: var(--icon-grey); stroke-width: 5; stroke-linecap: round; stroke-linejoin: round; }
  .company-mark {
    position: absolute;
    left: 0;
    top: 1108px;
    width: 927px;
    display: flex;
    justify-content: center;
    align-items: center;
    gap: 14px;
  }
  .company-mark__dot {
    width: 50px;
    height: 50px;
    border-radius: 50%;
    background: var(--ink-dark);
  }
  .company-mark__name {
    font-family: "Roboto Slab", Georgia, serif;
    font-weight: 400;
    font-size: 26px;
    letter-spacing: 1px;
    color: var(--ink-dark);
  }
</style>
</head>
<body>
<main class="poster">
  <div class="rule rule--top"></div>
  <header class="header-band">
    <h1 class="headline">OUR 5 WINNING NORMS</h1>
    <p class="subline">OWNing the P.A.T.H. to Tier 1</p>
  </header>
  <div class="rule rule--bottom"></div>

  <svg class="norm-wheel" viewBox="0 0 927 1200" aria-label="Five norms wheel: Ownership, Positive Mindset, Actions, Teamwork, Honesty">
    <defs>
      <path id="label-ring" d="M445,311 A325,325 0 1,1 444.9,311"/>
    </defs>

    <circle cx="445" cy="636" r="308" fill="none" stroke="var(--norm-blue)" stroke-width="5"/>
    <circle class="segment" cx="445" cy="636" r="300"/>

    <g class="divider">
      <line x1="445" y1="636" x2="445.0" y2="330"/>
      <line x1="445" y1="636" x2="736.0" y2="541.4"/>
      <line x1="445" y1="636" x2="624.9" y2="883.6"/>
      <line x1="445" y1="636" x2="265.1" y2="883.6"/>
      <line x1="445" y1="636" x2="154.0" y2="541.4"/>
    </g>
    <circle cx="445" cy="636" r="304" fill="none" stroke="var(--paper)" stroke-width="4"/>

    <!-- Ownership: single person -->
    <g class="icon">
      <circle cx="548" cy="417" r="12"/>
      <rect x="530" y="432" width="36" height="50" rx="6"/>
      <rect x="522" y="434" width="8" height="44" rx="4"/>
      <rect x="566" y="434" width="8" height="44" rx="4"/>
      <rect x="532" y="478" width="15" height="68" rx="2"/>
      <rect x="549" y="478" width="15" height="68" rx="2"/>
    </g>

    <!-- Positive mindset: plus in circle -->
    <circle class="icon-line" cx="630" cy="692" r="46"/>
    <path class="icon-line" d="M630,675 V709 M613,692 H647" stroke-width="4"/>

    <!-- Actions: gear -->
    <g class="icon" transform="translate(445 815)">
      <circle r="50"/>
      <rect x="-11" y="-64" width="22" height="24" rx="3"/>
      <rect x="-11" y="-64" width="22" height="24" rx="3" transform="rotate(30)"/>
      <rect x="-11" y="-64" width="22" height="24" rx="3" transform="rotate(60)"/>
      <rect x="-11" y="-64" width="22" height="24" rx="3" transform="rotate(90)"/>
      <rect x="-11" y="-64" width="22" height="24" rx="3" transform="rotate(120)"/>
      <rect x="-11" y="-64" width="22" height="24" rx="3" transform="rotate(150)"/>
      <rect x="-11" y="-64" width="22" height="24" rx="3" transform="rotate(180)"/>
      <rect x="-11" y="-64" width="22" height="24" rx="3" transform="rotate(210)"/>
      <rect x="-11" y="-64" width="22" height="24" rx="3" transform="rotate(240)"/>
      <rect x="-11" y="-64" width="22" height="24" rx="3" transform="rotate(270)"/>
      <rect x="-11" y="-64" width="22" height="24" rx="3" transform="rotate(300)"/>
      <rect x="-11" y="-64" width="22" height="24" rx="3" transform="rotate(330)"/>
      <circle r="17" fill="var(--norm-blue)"/>
    </g>

    <!-- Teamwork: three people -->
    <g class="icon">
      <circle cx="211" cy="648" r="11"/>
      <rect x="190" y="662" width="44" height="36" rx="8"/>
      <rect x="199" y="694" width="26" height="58" rx="2"/>
      <circle cx="259" cy="632" r="12"/>
      <rect x="237" y="647" width="45" height="40" rx="8"/>
      <rect x="246" y="684" width="27" height="69" rx="2"/>
      <circle cx="307" cy="652" r="11"/>
      <rect x="286" y="666" width="43" height="34" rx="8"/>
      <rect x="294" y="696" width="27" height="56" rx="2"/>
    </g>

    <!-- Honesty: tick in circle -->
    <circle class="icon-line" cx="327" cy="481" r="49"/>
    <path class="icon-line" d="M305,483 L321,499 L351,465" stroke-width="6"/>

    <!-- Ring labels -->
    <text class="norm-label">
      <textPath href="#label-ring" startOffset="11.1%" text-anchor="middle"><tspan class="norm-initial">OWN</tspan>ERSHIP</textPath>
    </text>
    <text class="norm-label">
      <textPath href="#label-ring" startOffset="32.5%" text-anchor="middle"><tspan class="norm-initial">P</tspan>OSITIVE MINDSET</textPath>
    </text>
    <text class="norm-label">
      <textPath href="#label-ring" startOffset="50%" text-anchor="middle"><tspan class="norm-initial">A</tspan>CTIONS</textPath>
    </text>
    <text class="norm-label">
      <textPath href="#label-ring" startOffset="72.5%" text-anchor="middle"><tspan class="norm-initial">T</tspan>EAMWORK</textPath>
    </text>
    <text class="norm-label">
      <textPath href="#label-ring" startOffset="90.3%" text-anchor="middle"><tspan class="norm-initial">H</tspan>ONESTY</textPath>
    </text>
  </svg>

  <footer class="company-mark">
    <span class="company-mark__dot"></span>
    <span class="company-mark__name">Morvane &amp; Tolbrick</span>
  </footer>
</main>
</body>
</html>
```